Author/ Speaker Business Card design

I need a business card designed that will go with the branding that is already on my book and website. I like clean and straightforward, but I am not opposed to something more 'innovative'.

Target Market(s)

Colleges and Universities, educational institutions

Industry/Entity Type

Education

Contact Information for Business Card

Standard size. It should be able to be printed on good quality white or ivory paper.

Font styles to use
Sans Serif

Colors
0355a3

Requirements
Must have
• There's a blue on my website. It should have some blue. My logo is at the top. It should have the logo incorporated somewhere on it. My name, Author | Speaker | Teacher | Trainer, my phone number (+31 64-207 5819), my email address (milo@theboldlearner.example), Social media icons (twitter, Instagram, LinkedIn) with the addresses (twitter @writermilofenwick, Instagram - theboldlearner, LinkedIn - theboldlearner) By they way, the website is www.theboldlearner.example. There is a photo of the book on the website. Also, my full name is Milo Fenwick
Nice to have
• Try to use the font that is on the website and book. Also, if you could get that blue, that would be great.
Should not have
• My photo

```html
<!DOCTYPE html>
<html lang="en">
<head>
<meta charset="utf-8">
<title>The Bold Learner – Business Card</title>
<link rel="stylesheet" href="https://fonts.googleapis.com/css2?family=Jost:wght@400;500;700&display=swap">
<style>
  :root {
    --brand-blue: #0355a3;
    --brand-blue-light: #1e7fdc;
    --ink: #3c4046;
    --paper: #ffffff;
    --backdrop: #e9ebee;
  }
  * { margin: 0; padding: 0; box-sizing: border-box; }
  html, body {
    width: 1200px; height: 900px; overflow: hidden;
    background: var(--backdrop);
    font-family: "Jost", "Futura", sans-serif;
  }
  .canvas { position: relative; width: 1200px; height: 900px; }

  .card {
    position: absolute;
    width: 630px; height: 360px;
    box-shadow: 0 10px 30px rgba(0,0,0,0.18);
  }

  /* Front */
  .card-front {
    left: 70px; top: 60px;
    background: linear-gradient(110deg, var(--brand-blue-light) 0%, var(--brand-blue) 60%);
    display: flex; align-items: center; justify-content: center;
  }
  .front-wordmark {
    color: var(--paper);
    font-weight: 700;
    font-size: 58px;
    letter-spacing: -0.5px;
  }

  /* Back */
  .card-back {
    left: 500px; top: 480px;
    background: var(--paper);
  }
  .back-wordmark {
    position: absolute; right: 34px; top: 42px;
    display: flex; align-items: center; gap: 10px;
    color: var(--brand-blue);
    font-weight: 500;
    font-size: 30px;
    line-height: 1;
  }
  .wordmark-dot {
    width: 16px; height: 16px; border-radius: 50%;
    background: var(--brand-blue);
  }

  .accent-bar {
    position: absolute; left: 0; top: 186px;
    width: 12px; height: 30px;
    background: var(--brand-blue);
  }
  .identity { position: absolute; left: 36px; top: 180px; }
  .person-name {
    color: var(--brand-blue);
    font-weight: 700;
    font-size: 24px;
    letter-spacing: 0.5px;
    text-transform: uppercase;
    line-height: 1.1;
  }
  .person-roles {
    color: var(--ink);
    font-size: 17px;
    margin-top: 2px;
  }
  .contact-list {
    list-style: none;
    margin-top: 12px;
    color: var(--ink);
    font-size: 14.5px;
  }
  .contact-list li {
    display: flex; align-items: center; gap: 9px;
    height: 21px;
  }
  .contact-icon { width: 13px; height: 13px; flex: none; fill: var(--brand-blue); }
  .social-square {
    width: 13px; height: 13px; flex: none;
    background: var(--brand-blue); border-radius: 2px;
  }
</style>
</head>
<body>
<main class="canvas">

  <section class="card card-front" aria-label="Card front">
    <span class="front-wordmark">The Bold Learner</span>
  </section>

  <section class="card card-back" aria-label="Card back">
    <div class="back-wordmark">
      <span class="wordmark-dot"></span>
      <span>The Bold Learner</span>
    </div>

    <div class="accent-bar"></div>

    <div class="identity">
      <h1 class="person-name">Milo Fenwick</h1>
      <p class="person-roles">Author | Speaker | Teacher | Trainer</p>

      <ul class="contact-list">
        <li>
          <svg class="contact-icon" viewBox="0 0 24 24" aria-hidden="true"><path d="M6.6 10.8a15.1 15.1 0 0 0 6.6 6.6l2.2-2.2a1 1 0 0 1 1-.25 11.4 11.4 0 0 0 3.6.57 1 1 0 0 1 1 1V20a1 1 0 0 1-1 1A17 17 0 0 1 3 4a1 1 0 0 1 1-1h3.5a1 1 0 0 1 1 1c0 1.25.2 2.45.57 3.57a1 1 0 0 1-.25 1z"/></svg>
          <span>+31 64-207 5819</span>
        </li>
        <li>
          <svg class="contact-icon" viewBox="0 0 24 24" aria-hidden="true"><path d="M2 5h20v14H2z M3.5 6.5 12 13l8.5-6.5" fill="var(--brand-blue)"/><path d="M3 6l9 7 9-7" fill="none" stroke="#fff" stroke-width="1.6"/></svg>
          <span>milo@theboldlearner.example</span>
        </li>
        <li>
          <svg class="contact-icon" viewBox="0 0 24 24" aria-hidden="true"><circle cx="12" cy="12" r="11"/><path d="M1 12h22M12 1c4 4 4 18 0 22M12 1c-4 4-4 18 0 22" fill="none" stroke="#fff" stroke-width="1.4"/></svg>
          <span>www.theboldlearner.example</span>
        </li>
        <li>
          <span class="social-square" aria-hidden="true"></span>
          <span>@writermilofenwick</span>
        </li>
        <li>
          <span class="social-square" aria-hidden="true"></span>
          <span class="social-square" aria-hidden="true"></span>
          <span>theboldlearner</span>
        </li>
      </ul>
    </div>
  </section>

</main>
</body>
</html>
```